Whitcombe Framing Works - Card Design

I am looking to use the logo designs that you already did for me to develop a business card. I would like the card to have a black background and be double sided. I want white and green logo and text. I have attached an inspiration photo of a look that I like. I would like to use the Vertical Logo attached to take up the full front side of the card. On the back where I have my name and information, I would like to have the horizontal logo or maybe even just the image of the 'A' and trees without the text. I am open, but I am looking for something clean and simple and I want the green to really pop! Additional files can be found under Design #: 40593216

Target Market(s)

Homeowners

Industry/Entity Type

Construction

Contact Information for Business Card

Name: Marcus Pellow, Title: Project Manager, Phone: 831.555.0147, Email: whitcombeframingworks@mailbarn.net, address: 418 Juniper Ln, Felton, CA 95092, Lic# 2046318

Colors
00AB8E
00BBA5
67D7C9
C6EFE9
E9F9F6

Requirements
Nice to have
• I would like to see the logos that I have already got from SketchHarbor, though I am open to new ones

```html
<!DOCTYPE html>
<html lang="en">
<head>
<meta charset="utf-8">
<title>Whitcombe Framing Works – Business Card</title>
<link href="https://fonts.googleapis.com/css2?family=Oswald:wght@300;400;500;600&display=swap" rel="stylesheet">
<style>
  :root {
    --stage: #d9d9d9;
    --card: #0f1418;
    --green: #66ff22;
    --white: #ffffff;
  }
  * { margin: 0; padding: 0; box-sizing: border-box; }
  html, body { width: 1200px; height: 846px; overflow: hidden; }
  body { background: var(--stage); position: relative; font-family: "Oswald", sans-serif; }

  .card {
    position: absolute;
    left: 347px;
    width: 509px;
    height: 291px;
    background: var(--card);
  }
  .card--info { top: 99px; }
  .card--brand { top: 457px; }

  /* info side */
  .brand-name-block {
    position: absolute;
    left: 36px; top: 116px;
    width: 188px; height: 106px;
    display: flex; align-items: center; gap: 12px;
  }
  .brand-name-block .mark-square {
    width: 44px; height: 44px; background: var(--green); flex: none;
  }
  .brand-name-block .brand-name {
    color: var(--white); font-weight: 600; font-size: 21px;
    line-height: 1.05; text-transform: uppercase; letter-spacing: 0.5px;
  }

  .contact {
    position: absolute;
    left: 241px; top: 108px;
  }
  .contact .person {
    color: var(--green); font-weight: 600; font-size: 19px;
    letter-spacing: 0.3px; line-height: 22px; text-transform: uppercase;
  }
  .contact .role {
    color: var(--white); font-weight: 300; font-style: italic;
    font-size: 13px; line-height: 18px; margin-top: 1px;
  }
  .contact ul { list-style: none; margin-top: 8px; }
  .contact li {
    display: flex; align-items: center; gap: 8px;
    color: var(--white); font-weight: 300; font-size: 15px;
    line-height: 22px; letter-spacing: 0.2px;
  }
  .contact li svg { width: 17px; height: 17px; flex: none; fill: var(--green); }

  /* brand side */
  .brand-mark {
    position: absolute;
    left: 234px; top: 84px;
    width: 44px; height: 44px; background: var(--green);
  }
  .est {
    position: absolute; top: 118px; width: 50px;
    color: var(--white); font-size: 11px; font-weight: 400;
    letter-spacing: 4px; text-align: center; line-height: 14px;
    border-top: 1px solid var(--green); border-bottom: 1px solid var(--green);
    padding: 4px 0;
  }
  .est--label { left: 110px; }
  .est--year { left: 346px; }

  .wordmark {
    position: absolute; left: 0; right: 0; top: 160px;
    text-align: center; color: var(--white); font-weight: 500;
    text-transform: uppercase;
  }
  .wordmark .line-main { font-size: 38px; line-height: 42px; letter-spacing: 2px; }
  .wordmark .line-sub { font-size: 17px; line-height: 20px; letter-spacing: 8px; }
</style>
</head>
<body>

<section class="card card--info">
  <div class="brand-name-block">
    <span class="mark-square"></span>
    <span class="brand-name">Whitcombe<br>Framing<br>Works</span>
  </div>

  <div class="contact">
    <p class="person">Marcus Pellow</p>
    <p class="role">Project Manager / Lic# 2046318</p>
    <ul>
      <li>
        <svg viewBox="0 0 24 24" aria-hidden="true"><path d="M6.6 10.8c1.4 2.8 3.8 5.1 6.6 6.6l2.2-2.2c.3-.3.7-.4 1-.2 1.1.4 2.3.6 3.6.6.6 0 1 .4 1 1V20c0 .6-.4 1-1 1C10.6 21 3 13.4 3 4c0-.6.4-1 1-1h3.5c.6 0 1 .4 1 1 0 1.3.2 2.5.6 3.6.1.3 0 .7-.2 1z"/></svg>
        831.555.0147
      </li>
      <li>
        <svg viewBox="0 0 24 24" aria-hidden="true"><path d="M2 5h20v14H2z M4 7v.4l8 5.6 8-5.6V7z" fill-rule="evenodd"/></svg>
        whitcombeframingworks@mailbarn.net
      </li>
      <li>
        <svg viewBox="0 0 24 24" aria-hidden="true"><path d="M12 3l10 9h-3v9h-5v-6h-4v6H5v-9H2z"/></svg>
        418 Juniper Ln, Felton, CA 95092
      </li>
    </ul>
  </div>
</section>

<section class="card card--brand">
  <span class="brand-mark"></span>
  <p class="est est--label">ESTD</p>
  <p class="est est--year">2020</p>
  <div class="wordmark">
    <p class="line-main">Whitcombe</p>
    <p class="line-sub">Framing Works</p>
  </div>
</section>

</body>
</html>
```